BUSINESS CARD DESIGN

NAME- TODD MASVERIK
PHONE NUMER - 808- 451-7082
EMAIL- OFFICE@VORLINDE-GRADEWAY.COM
BACK OF CARD- SPEACIALIZES IN LAND CLEARING, FORESTRY MUCLHING AND EXCAVATION

Contact Information for Business Card

NAME- TODD MASVERIK PHONE NUMER - 808- 451-7082 EMAIL- OFFICE@VORLINDE-GRADEWAY.COM BACK OF CARD- SPEACIALIZES IN LAND CLEARING , MUCLHING AND EXCAVATION

```html
<!DOCTYPE html>
<html lang="en">
<head>
<meta charset="utf-8">
<title>Vorlinde Gradeway — Business Card</title>
<link href="https://fonts.googleapis.com/css2?family=Montserrat:wght@400;500;700&display=swap" rel="stylesheet">
<style>
  :root {
    --backdrop: #9b9b9b;
    --card-white: #ffffff;
    --ink: #1c1c1c;
    --accent: #f5a81c;
    --card-black: #0f1010;
    --pattern-light: #2a2b2b;
    --pattern-dark: #0b0b0b;
    --mark-white: #f2f2f2;
    --muted-light: #8a8b8b;
  }
  * { margin: 0; padding: 0; box-sizing: border-box; }
  html, body { width: 1093px; height: 1200px; overflow: hidden; }
  body {
    background: var(--backdrop);
    font-family: "Montserrat", Arial, sans-serif;
    color: var(--ink);
    position: relative;
  }
  .card {
    position: absolute;
    left: 264px;
    width: 597px;
    box-shadow: 0 1px 4px rgba(0,0,0,.45);
  }
  .card--front { top: 224px; height: 364px; background: var(--card-white); }
  .card--back { top: 614px; height: 368px; background: var(--card-black); overflow: hidden; }

  .holder { position: absolute; left: 35px; top: 52px; }
  .holder__name {
    font-weight: 700; font-size: 22px; color: var(--accent);
    letter-spacing: .3px; line-height: 1;
  }
  .holder__title { font-size: 14px; font-weight: 400; margin-top: 6px; }

  .brand { position: absolute; left: 412px; top: 14px; width: 160px; text-align: center; }
  .brand__dot { width: 70px; height: 70px; border-radius: 50%; background: var(--ink); margin: 0 auto 14px; }
  .brand__name { font-weight: 700; font-size: 14px; line-height: 1.15; letter-spacing: 1px; color: var(--ink); }

  .contacts { position: absolute; left: 35px; top: 268px; list-style: none; }
  .contacts li { display: flex; align-items: center; height: 23.3px; font-size: 14px; }
  .contacts svg { width: 13px; height: 13px; margin-right: 7px; flex: none; }

  .address {
    position: absolute; left: 416px; top: 300px;
    font-size: 14px; line-height: 1.2; font-style: normal; white-space: nowrap;
  }

  .pattern {
    position: absolute; inset: 0;
    background: linear-gradient(120deg, var(--pattern-light) 0%, #1a1b1b 35%, var(--pattern-dark) 70%);
  }
  .back-mark {
    position: absolute; left: 418px; top: 240px; width: 110px;
    text-align: center; color: var(--mark-white);
    font-weight: 700; font-size: 12px; line-height: 1.2; letter-spacing: .8px;
  }
  .specialties {
    position: absolute; left: 0; right: 0; bottom: 22px;
    text-align: center; color: var(--muted-light);
    font-size: 11px; font-weight: 500; letter-spacing: 1.2px;
  }
</style>
</head>
<body>
  <section class="card card--front">
    <div class="holder">
      <h1 class="holder__name">TODD MASVERIK</h1>
      <p class="holder__title">Managing Director</p>
    </div>

    <div class="brand">
      <div class="brand__dot"></div>
      <p class="brand__name">VORLINDE<br>GRADEWAY LLC<br>808·451·7082</p>
    </div>

    <ul class="contacts">
      <li>
        <svg viewBox="0 0 16 16" aria-hidden="true"><path fill="var(--accent)" d="M3.5 1.5l2.3 2.4-1.3 1.8c.8 1.8 2.1 3.2 3.9 4.1l1.8-1.3 2.4 2.3-1.3 2.2C6.6 12.8 3 9.2 1.3 4.4z"/><path d="M9 2.5a5 5 0 0 1 4.5 4.5M9 .8a6.8 6.8 0 0 1 6.2 6.2" stroke="var(--accent)" stroke-width="1.3" fill="none"/></svg>
        808- 451-7082
      </li>
      <li>
        <svg viewBox="0 0 16 16" aria-hidden="true"><rect x="1" y="3" width="14" height="10" fill="var(--accent)"/><path d="M1 3.5l7 5 7-5" stroke="#fff" stroke-width="1.2" fill="none"/></svg>
        OFFICE@VORLINDE-GRADEWAY.COM
      </li>
      <li>
        <svg viewBox="0 0 16 16" aria-hidden="true"><circle cx="8" cy="8" r="7" fill="var(--accent)"/><path d="M1 8h14M8 1c-3 3.5-3 10.5 0 14M8 1c3 3.5 3 10.5 0 14" stroke="#fff" stroke-width="1" fill="none"/></svg>
        WWW.VORLINDE-GRADEWAY.COM
      </li>
    </ul>

    <address class="address">418 Kelmor Ave, #117<br>Dunwater, OH 43190</address>
  </section>

  <section class="card card--back">
    <div class="pattern" role="img" aria-label="Repeating glossy company emblem pattern fading from grey to black"></div>
    <p class="back-mark">VORLINDE<br>GRADEWAY</p>
    <p class="specialties">SPECIALIZES IN LAND CLEARING, FORESTRY MULCHING &amp; EXCAVATION</p>
  </section>
</body>
</html>
```